VELTRIX GROUP
Project: VXG LOGO
VXG LOGO - Trade
VXG LOGO
Use same font as used in my logo
FAISAL NOORi
GENERAL MANAGER
RIYADH
info@veltrixgroup-example.com
VXGROUP VXGROUP
following changes on your design no #158 the logo upper and left side of the letter head company name bottom and left side of the letter haead The business cards are also in the above pattern. waiting for your immediate response. thanks.

```html
<!DOCTYPE html>
<html lang="en">
<head>
<meta charset="utf-8">
<title>Veltrix Group – Business Card</title>
<link href="https://fonts.googleapis.com/css2?family=Saira:wght@600&display=swap" rel="stylesheet">
<style>
  :root {
    --brand-blue: #2f56a5;
    --card-white: #ffffff;
    --backdrop: #e4e5e7;
    --ink-light: #ffffff;
  }
  * { margin: 0; padding: 0; box-sizing: border-box; }
  html, body {
    width: 1200px;
    height: 837px;
    overflow: hidden;
    background: var(--backdrop);
    font-family: "Saira", sans-serif;
  }
  .business-card {
    position: absolute;
    left: 100px;
    top: 108px;
    width: 1000px;
    height: 620px;
    background: var(--card-white);
    color: var(--brand-blue);
  }
  .company-name {
    position: absolute;
    left: 32px;
    top: 28px;
    font-size: 42px;
    font-weight: 600;
    letter-spacing: 0.5px;
  }
  .brand-name {
    position: absolute;
    left: 0;
    right: 0;
    top: 170px;
    text-align: center;
    font-size: 120px;
    line-height: 1;
    font-weight: 600;
  }
  .person {
    position: absolute;
    right: 535px;
    top: 408px;
    text-align: right;
  }
  .person-name {
    font-size: 44px;
    font-weight: 600;
    line-height: 1;
    letter-spacing: 1px;
  }
  .person-role {
    font-size: 21px;
    font-weight: 600;
    letter-spacing: 1.5px;
    margin-top: 6px;
  }
  .divider {
    position: absolute;
    left: 498px;
    top: 392px;
    width: 4px;
    height: 125px;
    background: var(--brand-blue);
  }
  .contact {
    position: absolute;
    left: 580px;
    top: 392px;
    font-size: 31px;
    font-weight: 600;
    line-height: 42px;
    letter-spacing: 0.5px;
  }
  .contact-band {
    position: absolute;
    left: 0;
    right: 0;
    bottom: 0;
    height: 78px;
    background: var(--brand-blue);
    color: var(--ink-light);
    display: flex;
    align-items: center;
    justify-content: center;
    font-size: 28px;
    font-weight: 600;
    letter-spacing: 0.5px;
  }
</style>
</head>
<body>
  <div class="business-card">
    <div class="company-name">VELTRIX GROUP</div>
    <div class="brand-name">VXG</div>
    <div class="person">
      <div class="person-name">FAISAL NOORi</div>
      <div class="person-role">GENERAL MANAGER</div>
    </div>
    <div class="divider"></div>
    <div class="contact">
      <div class="contact-city">RIYADH</div>
      <div class="contact-phone">P: 966-100-2020</div>
      <div class="contact-fax">F: 966-100-3030</div>
    </div>
    <div class="contact-band">E: info@veltrixgroup-example.com</div>
  </div>
</body>
</html>
```